Life Insurance Landing Page (for lead gen)

We need a high converting life insurance page created. It will be housed at www.CoverCheckpoint.com. We will be driving former life insurance prospects to this page where they will only need to confirm their phone number & email in order to receive an updated quote.
Updates

Only the page design is required, the coding will be done on our end. 

Target Market(s)

People who have expressed an interest in obtaining life insurance.

Industry/Entity Type

Life Insurance

Requirements
Must have
• 1) Under "CoverCheckpoint.com" Please include a "Powered by TPVN" tag and match the colors of this site: http://thetpvn.com/life-insurance-services.html to the page.

2) The form should ask for their phone number and include an appointment calendar widget (we'll code the functionality) so they can choose the date/time of their call. It should also have an email confirmation field.

3) the overall message next to the form fields should be "Thanks for visiting Gordon (we'll personalize this "firstname" field ), please let us know the best time to schedule a brief call so we can give you an updated, rock bottom pricing quote on a policy. We'll also email you with the information, please confirm your email here and we'll send you the details.

4) We'd like to include a box that appears to be a personalized "quote briefing" snapshot that will list this information: "Name: _________" "Birth Date:"____________" "Policy Type: _______", "Coverage Amount: ____________" " all these fields will be populated into the page.

```html
<!DOCTYPE html>
<html lang="en">
<head>
<meta charset="utf-8">
<title>CoverCheckpoint.com – Life Insurance Quotes</title>
<link rel="stylesheet" href="https://fonts.googleapis.com/css2?family=Open+Sans:ital,wdth,wght@0,75..100,300..800;1,75..100,300..800&family=Ubuntu:wght@500;700&display=swap">
<style>
  :root {
    --orange: #f7931e;
    --orange-deep: #e8760a;
    --gold: #fcc01e;
    --text: #666666;
    --text-dark: #444444;
    --muted: #999999;
    --page: #ffffff;
    --panel-border: #d6d6d6;
    --input-border: #c8c8c8;
    --partner-grey: #cfcfcf;
    --social-blue: #2f5fa8;
    --tint: #fff6ea;
  }
  * { box-sizing: border-box; margin: 0; padding: 0; }
  html, body { width: 1024px; height: 1200px; overflow: hidden; background: var(--page); }
  body { position: relative; font-family: "Open Sans", Arial, sans-serif; color: var(--text); }
  .abs { position: absolute; }

  .brand { left: 136px; top: 18px; font-family: "Ubuntu", Arial, sans-serif; font-weight: 500; font-size: 20px; color: var(--orange); }
  .powered { left: 137px; top: 46px; font-size: 10px; color: var(--muted); letter-spacing: .3px; }
  .powered b { color: var(--orange-deep); font-weight: 700; }
  .quote-call { left: 650px; top: 9px; display: flex; align-items: center; gap: 8px; }
  .quote-call .icon { width: 43px; height: 43px; }
  .quote-call .label { font-family: "Ubuntu", Arial, sans-serif; font-weight: 500; font-size: 13px; color: var(--muted); letter-spacing: .3px; line-height: 1.2; }
  .quote-call .phone { font-family: "Ubuntu", Arial, sans-serif; font-weight: 700; font-size: 19px; color: var(--orange); letter-spacing: .4px; line-height: 1.1; }

  .hero-photo { left: 136px; top: 90px; width: 310px; height: 308px; border-radius: 120px 120px 0 0; background: linear-gradient(180deg, #d9cbb7 0%, #9ea4ab 55%, #2c3a5a 100%); }
  .hero-title { left: 464px; top: 168px; width: 400px; font-family: "Ubuntu", Arial, sans-serif; font-weight: 700; font-size: 25px; line-height: 31px; color: var(--orange); }
  .hero-sub { left: 463px; top: 243px; width: 440px; font-size: 14.5px; font-weight: 300; line-height: 20px; color: var(--text); }

  .briefing { left: 463px; top: 300px; width: 426px; height: 86px; border: 1px solid #f3d3a8; border-radius: 4px; background: var(--tint); padding: 8px 14px; }
  .briefing h3 { font-family: "Ubuntu", Arial, sans-serif; font-weight: 500; font-size: 12.5px; color: var(--orange-deep); margin-bottom: 6px; }
  .briefing dl { display: grid; grid-template-columns: 1fr 1fr; column-gap: 18px; row-gap: 7px; font-size: 10.5px; }
  .briefing div { display: flex; gap: 5px; align-items: flex-end; }
  .briefing dt { font-weight: 600; color: var(--text-dark); white-space: nowrap; }
  .briefing dd { flex: 1; height: 13px; border-bottom: 1px solid #d9b98c; }

  .panel { left: 133px; top: 398px; width: 757px; height: 758px; border: 1px solid var(--panel-border); background: #fff; box-shadow: 0 1px 3px rgba(0,0,0,.18); }

  .section-title { font-family: "Ubuntu", Arial, sans-serif; font-weight: 500; font-size: 19px; color: var(--orange-deep); }
  .about-title { left: 169px; top: 434px; }
  .about-photo { left: 164px; top: 477px; width: 367px; height: 137px; background: linear-gradient(90deg, #d8b89a 0%, #e7cdb3 45%, #c6d5e4 100%); }
  .about-text { left: 166px; top: 633px; width: 372px; font-size: 13px; line-height: 19.2px; color: var(--text); }

  .benefits-title { left: 170px; top: 782px; }
  .offer-title { left: 362px; top: 782px; }
  .list { list-style: none; font-size: 13px; line-height: 25.6px; }
  .list li { position: relative; padding-left: 25px; }
  .list li::before { content: ""; position: absolute; left: 4px; top: 9px; border-left: 5px solid #777; border-top: 4px solid transparent; border-bottom: 4px solid transparent; }
  .benefits { left: 170px; top: 830px; color: var(--text); }
  .offers { left: 363px; top: 830px; color: var(--text-dark); font-weight: 600; }

  .quote-form { left: 582px; top: 434px; width: 278px; height: 414px; }
  .quote-form > svg { position: absolute; left: 0; top: 0; }
  .form-head { position: absolute; left: 0; top: 12px; width: 276px; text-align: center; font-weight: 700; font-stretch: 75%; font-size: 27px; line-height: 26px; color: #fff; text-shadow: 0 1px 2px rgba(120,50,0,.5); }
  .form-note { position: absolute; left: 16px; top: 92px; width: 244px; font-size: 9.5px; line-height: 13px; color: var(--text-dark); }
  .form-note b { color: var(--orange-deep); }
  .field { position: absolute; left: 17px; width: 242px; height: 28px; border: 1px solid var(--input-border); border-radius: 2px; background: #fff; box-shadow: inset 0 1px 2px rgba(0,0,0,.08); padding-left: 11px; font-size: 10px; line-height: 26px; color: #777; }
  .field .req { color: #d0021b; }
  .cal-label { position: absolute; left: 17px; top: 265px; font-size: 9.5px; font-weight: 600; color: var(--text-dark); }
  .cal-label span { font-weight: 400; color: var(--muted); }
  .days { position: absolute; left: 17px; top: 281px; width: 242px; display: grid; grid-template-columns: repeat(5, 1fr); gap: 4px; }
  .days div { height: 30px; border: 1px solid var(--input-border); border-radius: 2px; background: #fff; text-align: center; font-size: 8px; line-height: 11px; padding-top: 3px; color: var(--muted); }
  .days div b { display: block; font-size: 11px; line-height: 13px; color: var(--text-dark); }
  .days .on { background: var(--orange); border-color: var(--orange-deep); color: #fff; }
  .days .on b { color: #fff; }
  .slots { position: absolute; left: 17px; top: 316px; width: 242px; display: grid; grid-template-columns: repeat(4, 1fr); gap: 4px; }
  .slots div { height: 20px; border: 1px solid var(--input-border); border-radius: 2px; background: #fff; text-align: center; font-size: 9px; line-height: 18px; color: var(--text-dark); }
  .slots .on { background: var(--orange); border-color: var(--orange-deep); color: #fff; }
  .submit { position: absolute; left: 58px; top: 346px; width: 161px; height: 36px; border: 1px solid #c77400; background: linear-gradient(180deg, var(--gold) 0%, var(--orange-deep) 100%); text-align: center; font-weight: 700; font-stretch: 75%; font-size: 20px; line-height: 34px; color: #fff; text-shadow: 0 1px 2px rgba(120,50,0,.5); }

  .testimonial-title { left: 582px; top: 866px; width: 276px; text-align: center; }
  .avatar { left: 642px; top: 904px; width: 62px; height: 62px; border-radius: 50%; background: radial-gradient(circle at 50% 45%, #c9946c 0%, #8a6347 60%, #4a4a4a 100%); }
  .client-name { left: 720px; top: 918px; font-size: 12.5px; font-weight: 600; color: #333; }
  .client-org { left: 722px; top: 937px; font-size: 10px; font-style: italic; color: var(--muted); }
  .client-quote { left: 613px; top: 976px; width: 238px; font-size: 10px; line-height: 16px; color: var(--text-dark); }

  .divider { left: 416px; top: 1044px; width: 196px; height: 1px; background: linear-gradient(90deg, transparent, #ddd, transparent); }
  .partners { left: 258px; top: 1064px; }

  .copyright { left: 131px; top: 1175px; font-size: 9.5px; color: #777; }
  .social { left: 817px; top: 1168px; display: flex; gap: 5px; }
  .social span { width: 21px; height: 21px; border-radius: 2px; background: var(--social-blue); box-shadow: 0 1px 2px rgba(0,0,0,.3); }
</style>
</head>
<body>
  <header>
    <div class="abs brand">CoverCheckpoint.com</div>
    <div class="abs powered">Powered by <b>TPVN</b></div>
    <div class="abs quote-call">
      <svg class="icon" viewBox="0 0 43 43" aria-hidden="true">
        <defs><linearGradient id="callGrad" x1="0" y1="0" x2="0" y2="1"><stop offset="0" stop-color="#fcd34a"/><stop offset="1" stop-color="#f39a12"/></linearGradient></defs>
        <circle cx="21.5" cy="21.5" r="21" fill="url(#callGrad)"/>
        <path d="M15 12c1.5-1 2.8-.6 3.4.6l1.4 2.8c.5 1 .1 2-.8 2.5l-1 .6c.6 2.8 2.4 5.3 4.9 6.8l.8-.9c.7-.8 1.8-.9 2.6-.2l2.4 2c1 .8 1 2.1.1 3.1-1.5 1.6-3.6 2.1-5.6 1.1-5-2.5-8.6-7.5-9.4-13-.3-2 .3-4 1.2-5.4z" fill="#e07a10"/>
      </svg>
      <div>
        <div class="label">Request a FREE Quote</div>
        <div class="phone">+1800.555.0142</div>
      </div>
    </div>
  </header>

  <section>
    <div class="abs hero-photo" role="img" aria-label="Photo of a smiling family of four embracing"></div>
    <h1 class="abs hero-title">Get FAST Quotes and SAVE Money on Your Life Insurance</h1>
    <p class="abs hero-sub">Life insurance gives you the peace of mind having the protection to your loved ones.</p>
    <aside class="abs briefing">
      <h3>Your Quote Briefing</h3>
      <dl>
        <div><dt>Name:</dt><dd></dd></div>
        <div><dt>Birth Date:</dt><dd></dd></div>
        <div><dt>Policy Type:</dt><dd></dd></div>
        <div><dt>Coverage Amount:</dt><dd></dd></div>
      </dl>
    </aside>
  </section>

  <main class="abs panel"></main>

  <h2 class="abs section-title about-title">About Life Insurance</h2>
  <div class="abs about-photo" role="img" aria-label="Photo of a happy family of four outdoors under a blue sky"></div>
  <p class="abs about-text">Lid est laborum dolo rumes fugats untras. Etharums ser quidem rerum facilis dolores nemis omnis fugats vitaes nemo minima rerums unsers sadips amets. Lid est laborum dolo rumes fugats untras. Etharums ser quidem rerum facilis dolores nemis omnis fugats vitaes nemo minima rerums unsers sadips amets.</p>

  <h2 class="abs section-title benefits-title">Key Benefits</h2>
  <ul class="abs list benefits">
    <li>Lid est laborum</li>
    <li>dolo rumes fugats</li>
    <li>Etharums ser quidem</li>
    <li>Rerum facilis dolores</li>
    <li>Nemis omnis fugats</li>
    <li>Vitaes nemo minima</li>
    <li>Rerums unsers sadips</li>
  </ul>

  <h2 class="abs section-title offer-title">What We Offer</h2>
  <ul class="abs list offers">
    <li>Auto Insurance</li>
    <li>Home Insurance</li>
    <li>Life Insurance</li>
    <li>Health Insurance</li>
    <li>Business Insurance</li>
    <li>Restaurant Insurance</li>
    <li>Workers Comp</li>
  </ul>

  <form class="abs quote-form">
    <svg width="278" height="414" viewBox="0 0 278 414" aria-hidden="true">
      <defs>
        <linearGradient id="headGrad" x1="0" y1="0" x2="0" y2="1"><stop offset="0" stop-color="#fcc01e"/><stop offset="1" stop-color="#e06a00"/></linearGradient>
        <linearGradient id="bodyGrad" x1="0" y1="0" x2="0" y2="1"><stop offset="0" stop-color="#f7f7f7"/><stop offset="1" stop-color="#ececec"/></linearGradient>
      </defs>
      <path d="M0 60 H276 V392 L138 412 L0 392 Z" fill="#d0d0d0" transform="translate(2 0)"/>
      <path d="M0 60 H276 V392 L138 410 L0 392 Z" fill="url(#bodyGrad)"/>
      <path d="M0 4 Q0 0 4 0 H272 Q276 0 276 4 V62 L138 86 L0 62 Z" fill="url(#headGrad)"/>
    </svg>
    <div class="form-head">GET A QUOTATION<br>FOR FREE!</div>
    <p class="form-note">Thanks for visiting <b>Gordon</b>, please let us know the best time to schedule a brief call so we can give you an updated, rock bottom pricing quote on a policy. We'll also email you with the information, please confirm your email here and we'll send you the details.</p>
    <div class="field" style="top:164px">Phone<span class="req">*</span></div>
    <div class="field" style="top:197px">Email<span class="req">*</span></div>
    <div class="field" style="top:230px">Confirm Email<span class="req">*</span></div>
    <div class="cal-label">Schedule your call <span>– pick a date &amp; time</span></div>
    <div class="days">
      <div>MON<b>12</b></div>
      <div class="on">TUE<b>13</b></div>
      <div>WED<b>14</b></div>
      <div>THU<b>15</b></div>
      <div>FRI<b>16</b></div>
    </div>
    <div class="slots">
      <div>9:00 AM</div>
      <div class="on">11:00 AM</div>
      <div>2:00 PM</div>
      <div>4:00 PM</div>
    </div>
    <div class="submit">SUBMIT NOW</div>
  </form>

  <h2 class="abs section-title testimonial-title">Client Testimonial</h2>
  <div class="abs avatar" role="img" aria-label="Portrait photo of the client"></div>
  <div class="abs client-name">Daniel Reyes</div>
  <div class="abs client-org">Harbor Agency</div>
  <p class="abs client-quote">"Lorem ipsum dolor sit amet, consectetur adipisic-ing elit, sed do eiusmod tempor incididunt ut labore et dolore magna aliqua."</p>

  <div class="abs divider"></div>
  <svg class="abs partners" width="510" height="70" viewBox="0 0 510 70" aria-label="Partner badges" role="img">
    <circle cx="32" cy="32" r="29" fill="var(--partner-grey)"/>
    <rect x="90" y="22" width="130" height="22" rx="4" fill="var(--partner-grey)"/>
    <rect x="250" y="6" width="56" height="56" fill="var(--partner-grey)"/>
    <rect x="336" y="14" width="82" height="40" rx="20" fill="var(--partner-grey)"/>
    <circle cx="474" cy="32" r="29" fill="var(--partner-grey)"/>
  </svg>

  <footer>
    <div class="abs copyright">Copyright 2014 CoverCheckpoint.com&nbsp;&nbsp;|&nbsp;&nbsp;All Rights Reserved</div>
    <div class="abs social" aria-label="Social links">
      <span></span><span></span><span></span>
    </div>
  </footer>
</body>
</html>
```